Supplement Manufacture needs a label designed

We need a label design done for a patented supplement for pain management. We would like to see designs that include a shade of blue as the main color. We would like the label to be noticeable amongst the crowded field and position our product to be selected based on the beauty of the label. We have attached a label that we created but it is not what we need but it shows the color blue we prefer. Please visit our website for more information. www.brokaleaf.net.

Target Market(s)

Health conscious individuals, Individuals who are looking for 100% all natural supplements.

Industry/Entity Type

Health And Wellness

Font styles to use
Serif

Colors
2f74b4
9bcb3c
f8a142
fbed22

Requirements
Must have
• Must have professional look and fit on 150cc HDPE packer bottle. Must meet US QHW label requirements.

```html
<!DOCTYPE html>
<html lang="en">
<head>
<meta charset="utf-8">
<title>Veltra Neuromuscular Support Label</title>
<link href="https://fonts.googleapis.com/css2?family=Montserrat:ital,wght@0,400;0,500;0,600;0,700;1,400;1,600;1,700&display=swap" rel="stylesheet">
<style>
  :root {
    --page: #ececec;
    --ink: #0c0c2e;
    --blue-deep: #1a7ee0;
    --blue-mid: #3fb2ee;
    --blue-light: #9fe2f6;
    --blue-pale: #d6eef6;
    --rule: #46c6ee;
    --white: #ffffff;
  }
  * { box-sizing: border-box; margin: 0; padding: 0; }
  html, body { width: 1200px; height: 1200px; overflow: hidden; background: var(--page); }
  body { font-family: "Montserrat", sans-serif; color: var(--ink); position: relative; }

  .label {
    position: absolute; left: 0; top: 350px; width: 1200px; height: 500px;
    background: linear-gradient(100deg, var(--blue-deep) 0%, var(--blue-mid) 30%, var(--blue-light) 62%, var(--blue-pale) 82%, var(--blue-light) 100%);
    overflow: hidden;
  }
  .label-art { position: absolute; inset: 0; }
  .panel { position: absolute; top: 15px; height: 473px; border: 1.5px solid var(--ink); }
  .panel-front { left: 15px; width: 370px; }
  .panel-facts { left: 415px; width: 370px; height: 288px; padding: 5px; }
  .panel-info { left: 815px; width: 371px; }

  .brand { position: absolute; left: 21px; top: 70px; display: flex; align-items: center; gap: 8px; }
  .brand-name { font-weight: 700; font-size: 34px; letter-spacing: 1px; color: var(--ink); }
  .brand-mark { width: 12px; height: 12px; background: var(--ink); }
  .tagline { position: absolute; left: 21px; top: 117px; font-weight: 600; font-size: 13.5px; line-height: 16px; text-transform: uppercase; }
  .actives { position: absolute; left: 21px; top: 180px; font-size: 13px; line-height: 14.5px; font-style: italic; text-transform: uppercase; list-style: none; }
  .actives b { font-weight: 700; }
  .blocks { position: absolute; left: 20px; top: 275px; width: 130px; height: 110px; background: var(--ink); opacity: .9; }
  .front-foot { position: absolute; left: 200px; width: 167px; top: 438px; text-align: right; font-size: 11.5px; text-transform: uppercase; line-height: 14px; }
  .front-foot b { font-weight: 700; font-style: italic; }

  .facts-card { background: var(--white); height: 100%; padding: 17px 7px 0 8px; font-size: 8.2px; text-transform: uppercase; overflow: hidden; }
  .facts-title { font-weight: 700; font-size: 25px; letter-spacing: .5px; line-height: 30px; margin-bottom: 8px; }
  .facts-meta { line-height: 12px; }
  .facts-meta .dv { float: right; }
  .facts-table { width: 100%; border-collapse: collapse; margin-top: 1px; }
  .facts-table td { border-top: 1.2px solid var(--rule); padding: 2.5px 0 2.5px; vertical-align: top; line-height: 10px; }
  .facts-table td.amt { text-align: right; width: 48px; white-space: nowrap; padding-right: 14px; }
  .facts-table td.pct { text-align: right; width: 34px; }
  .facts-note { font-style: italic; border-top: 1.2px solid var(--rule); padding-top: 3px; line-height: 10px; }
  .facts-other { margin-top: 8px; line-height: 10px; }
  .patent { position: absolute; left: 415px; top: 312px; width: 368px; text-align: right; font-weight: 700; font-size: 12.5px; }

  .info { position: absolute; left: 831px; top: 84px; width: 330px; font-weight: 700; font-size: 12.5px; line-height: 16.5px; text-transform: uppercase; }
  .info p { margin-bottom: 7px; }
  .info .disclaimer { font-weight: 400; font-style: italic; font-size: 10.5px; line-height: 14px; margin-top: 9px; }
  .maker { position: absolute; left: 1004px; top: 385px; font-weight: 700; font-size: 10px; line-height: 13.5px; text-transform: uppercase; }
  .maker .contact { margin-top: 13px; }
</style>
</head>
<body>
  <section class="label">
    <div class="label-art" role="img" aria-label="Blue background illustration of a glowing DNA double helix with scattered light particles"></div>

    <div class="panel panel-front"></div>
    <div class="brand"><span class="brand-name">VELTRA</span><span class="brand-mark"></span></div>
    <div class="tagline">Neuromuscular Support<br>Natural Muscle &amp; Joint Formula</div>
    <ul class="actives">
      <li><b>*Tumeric</b> (Extract 95% Curcuminoids)</li>
      <li><b>*Boswellia</b> (Extract 65% Boswellic Acids)</li>
      <li><b>*Bromelain</b></li>
      <li><b>*Quercetin</b></li>
    </ul>
    <div class="blocks" role="img" aria-label="Dark block graphic emblem"></div>
    <div class="front-foot">Dietary Supplement<br><b>60 Capsules</b></div>

    <div class="panel panel-facts">
      <div class="facts-card">
        <h2 class="facts-title">SUPPLEMENT FACTS</h2>
        <div class="facts-meta"><b>Serving Size</b> : 1 Capsule<br>Amount Per Serving <span class="dv">%DV</span></div>
        <table class="facts-table">
          <tr><td>Thiamin (as Thiamin Hydrochloride USP)</td><td class="amt">25 MG</td><td class="pct">1667%</td></tr>
          <tr><td>Vitamin B6 (as Pyridoxine Hydrochloride USP)</td><td class="amt">25 MG</td><td class="pct">1250%</td></tr>
          <tr><td>DLPA (DL - Phenylalanine)</td><td class="amt">75 MG</td><td class="pct">*</td></tr>
          <tr><td>Turmenic (Curcuma Longa) Root, Dried Extract,<br>Dried Extract, Min 95% Curcuminoids</td><td class="amt">200 MG</td><td class="pct">*</td></tr>
          <tr><td>Boswellia Serrata Gum Resin, Dried Extract,<br>Min 65% Boswellic Acids</td><td class="amt">175 MG</td><td class="pct">*</td></tr>
          <tr><td>Bromelain (from Pineapple)</td><td class="amt">125 MG</td><td class="pct">*</td></tr>
          <tr><td>Quercetin (as Quercetin Dehydrate)</td><td class="amt">75 MG</td><td class="pct">*</td></tr>
        </table>
        <div class="facts-note">*Daily Value Not Established</div>
        <div class="facts-other">Other Ingredients : <b>Vegetarian Capsules</b></div>
      </div>
    </div>
    <div class="patent">PATENET NO. 8123456</div>

    <div class="panel panel-info"></div>
    <div class="info">
      <p>Sugested Use :<br>1 to 2 capsules in morning and night,<br>not to exceed 6 capsules per day.</p>
      <p>Do not use if full-bottle shrink-wrap<br>is broken or missing.</p>
      <p>Store in cool, dry place (59” F - 85” F)<br>away from direct light.<br>Keep out of reach of children</p>
      <p>This product was made in QHW and GMP<br>9001 : 2000 registered facility.</p>
      <p class="disclaimer">These statements have not been evaluated<br>by the QHW.<br>This product is not intended to diagnose,<br>cure or prevent any disease.</p>
    </div>
    <div class="maker">
      Manufactured for :<br>Corvane, LLC.<br>Elmbrook, GA 30000
      <div class="contact">1-800-555-0142<br>www.brokaleaf.net</div>
    </div>
  </section>
</body>
</html>
```